Brightbay Business Card Design

Our company is called Brightbay. We manufacture confectionary snacks & frozen novelties. Our initial product portfolio includes frozen ice lollies/popsicles & stick ice cream bars.

We require a business card design.

Please use the attached Logo.

Please use an orange, brown, yellow colour code. You may choose any combination of the 3 or include all three. The logo however must remain orange.

Target Market(s)

Business card will be targeted at distributors of our products such as supermarket procurement managers, convenience store owners, wholesale distributors and merchandising agents.

Industry/Entity Type

Business

Requirements
Must have
• Calvin Obeng_Director/ P.O.Box Dunmore 5172, Accra, Ghana / m: 00233(0)507318924/ e: calvin.obeng@mailvora.co.uk

```html
<!DOCTYPE html>
<html lang="en">
<head>
<meta charset="utf-8">
<title>Brightbay Business Card</title>
<link rel="stylesheet" href="https://fonts.googleapis.com/css2?family=Roboto+Condensed:ital,wght@0,500;0,700;1,700&display=swap">
<style>
  :root {
    --page: #ffffff;
    --card-orange: #f37021;
    --pattern-orange: #e4532a;
    --ink-light: #ffffff;
  }
  * { margin: 0; padding: 0; box-sizing: border-box; }
  html, body {
    width: 767px;
    height: 1200px;
    overflow: hidden;
    background: var(--page);
  }
  .canvas {
    position: relative;
    width: 767px;
    height: 1200px;
  }
  .card {
    position: absolute;
    left: 99px;
    top: 102px;
    width: 569px;
    height: 995px;
    overflow: hidden;
    font-family: "Roboto Condensed", "Arial Narrow", sans-serif;
    color: var(--ink-light);
    text-align: center;
  }
  .card__pattern {
    position: absolute;
    inset: 0;
    background:
      radial-gradient(ellipse 70% 40% at 30% 25%, rgba(228, 83, 42, 0.55), rgba(228, 83, 42, 0) 70%),
      radial-gradient(ellipse 70% 40% at 70% 60%, rgba(228, 83, 42, 0.5), rgba(228, 83, 42, 0) 70%),
      radial-gradient(ellipse 70% 35% at 40% 92%, rgba(228, 83, 42, 0.45), rgba(228, 83, 42, 0) 70%),
      linear-gradient(180deg, var(--card-orange) 0%, #ee6526 50%, var(--card-orange) 100%);
  }
  .brand {
    position: absolute;
    left: 0;
    right: 0;
    top: 262px;
    font-weight: 700;
    font-size: 110px;
    line-height: 1;
    letter-spacing: 1px;
  }
  .contact {
    position: absolute;
    left: 0;
    right: 0;
    top: 649px;
    font-style: normal;
  }
  .contact__name {
    font-weight: 700;
    font-size: 36px;
    line-height: 40px;
  }
  .contact__role {
    font-weight: 700;
    font-style: italic;
    font-size: 28px;
    line-height: 30px;
    margin-bottom: 8px;
  }
  .contact__line {
    font-weight: 500;
    font-size: 27px;
    line-height: 36px;
  }
</style>
</head>
<body>
  <main class="canvas">
    <section class="card">
      <div class="card__pattern" role="img" aria-label="Repeating pattern of brand symbols on wavy bands in deeper orange over the orange card"></div>
      <h1 class="brand">Brightbay</h1>
      <address class="contact">
        <p class="contact__name">Calvin Obeng</p>
        <p class="contact__role">Director</p>
        <p class="contact__line">P.O.Box Dunmore 5172,</p>
        <p class="contact__line">Accra, Ghana</p>
        <p class="contact__line">m: 00233(0)507318924</p>
        <p class="contact__line">e: calvin.obeng@mailvora.co.uk</p>
      </address>
    </section>
  </main>
</body>
</html>
```